Copper Lane Assembly - Crossroads Waltz CD Cover

To prepare a CD Cover for the single "Crossroads Waltz" by Copper Lane Assembly.
You can hear the single here:
http://copperlaneassembly.example/listen/

The CLA logo and backdrop are also provided if you want to incorporate them into the CD cover design, though that isn't mandatory.

Song is about deciding on taking on a serious relationship, and leaving the single life behind.

Target Market(s)

Music listeners, 18-50 yrs old, into retro 80s, Tin Orchards/Surf Monks

Industry/Entity Type

Music Download

Requirements
Must have
• CLA logo
• Crossroads Waltz title
Nice to have
• Use of backdrop, or facimile
Should not have
• Too obvious on the term Crossroads Waltz

```html
<!DOCTYPE html>
<html lang="en">
<head>
<meta charset="utf-8">
<title>Copper Lane Assembly – Crossroads Waltz</title>
<link rel="stylesheet" href="https://fonts.googleapis.com/css2?family=Antonio:wght@300&family=Caveat+Brush&display=swap">
<style>
  :root {
    --page-bg: #1e212b;
    --sky-deep: #07080e;
    --sky-mid: #0c0e1c;
    --sky-glow: #2a2f8a;
    --sky-haze: #161a4a;
    --orb-light: #24524f;
    --orb-mid: #173c3d;
    --orb-dark: #0c2528;
    --ink-light: #ece9df;
  }
  html, body {
    margin: 0;
    padding: 0;
    width: 1200px;
    height: 1114px;
    overflow: hidden;
    background: var(--page-bg);
  }
  .cover {
    position: absolute;
    left: 134px;
    top: 94px;
    width: 936px;
    height: 902px;
    overflow: hidden;
    box-shadow: 0 14px 40px rgba(0, 0, 0, 0.45);
  }
  .cover-art {
    position: absolute;
    inset: 0;
    width: 936px;
    height: 902px;
    display: block;
  }
  .band-name {
    position: absolute;
    left: 681px;
    top: 94px;
    margin: 0;
    font-family: "Antonio", "Arial Narrow", sans-serif;
    font-weight: 300;
    font-size: 50px;
    line-height: 62px;
    letter-spacing: 0.5px;
    color: var(--ink-light);
    text-transform: uppercase;
  }
  .band-name span { display: block; }
  .single-title {
    position: absolute;
    left: 634px;
    width: 240px;
    top: 722px;
    margin: 0;
    text-align: center;
    font-family: "Caveat Brush", cursive;
    font-weight: 400;
    font-size: 30px;
    line-height: 38px;
    color: var(--ink-light);
    text-transform: lowercase;
  }
</style>
</head>
<body>
  <main class="cover">
    <svg class="cover-art" viewBox="0 0 936 902" xmlns="http://www.w3.org/2000/svg">
      <defs>
        <linearGradient id="sky-fill" x1="1" y1="0" x2="0" y2="1">
          <stop offset="0" stop-color="var(--sky-deep)"/>
          <stop offset="0.45" stop-color="var(--sky-mid)"/>
          <stop offset="1" stop-color="var(--sky-deep)"/>
        </linearGradient>
        <radialGradient id="sky-band" cx="0.5" cy="0.5" r="0.5">
          <stop offset="0" stop-color="var(--sky-glow)" stop-opacity="0.75"/>
          <stop offset="0.5" stop-color="var(--sky-haze)" stop-opacity="0.45"/>
          <stop offset="1" stop-color="var(--sky-haze)" stop-opacity="0"/>
        </radialGradient>
        <radialGradient id="orb-fill" cx="0.42" cy="0.38" r="0.72">
          <stop offset="0" stop-color="var(--orb-light)"/>
          <stop offset="0.55" stop-color="var(--orb-mid)"/>
          <stop offset="1" stop-color="var(--orb-dark)"/>
        </radialGradient>
      </defs>
      <g class="starfield" role="img" aria-label="Night sky starfield with a diagonal band of blue stars">
        <rect width="936" height="902" fill="url(#sky-fill)"/>
        <ellipse cx="420" cy="500" rx="560" ry="120" transform="rotate(-32 420 500)" fill="url(#sky-band)"/>
      </g>
      <g class="orb-grid" fill="url(#orb-fill)">
        <circle cx="172" cy="186" r="124" role="img" aria-label="Teal watercolour disc with floating iridescent bubbles"/>
        <circle cx="463" cy="186" r="124" role="img" aria-label="Teal watercolour disc with floating iridescent bubbles"/>
        <circle cx="754" cy="186" r="124" role="img" aria-label="Teal watercolour disc with floating iridescent bubbles"/>
        <circle cx="172" cy="462" r="124" role="img" aria-label="Teal watercolour disc with a large glowing bubble ring"/>
        <circle cx="463" cy="462" r="124" role="img" aria-label="Teal watercolour disc with floating iridescent bubbles"/>
        <circle cx="754" cy="462" r="124" role="img" aria-label="Teal watercolour disc with clustered iridescent bubbles"/>
        <circle cx="172" cy="738" r="124" role="img" aria-label="Teal watercolour disc with floating iridescent bubbles"/>
        <circle cx="463" cy="738" r="124" role="img" aria-label="Teal watercolour disc with floating iridescent bubbles"/>
        <circle cx="754" cy="738" r="124" role="img" aria-label="Teal watercolour disc with floating iridescent bubbles"/>
      </g>
    </svg>
    <h1 class="band-name"><span>Copper</span><span>Lane</span><span>Assembly</span></h1>
    <h2 class="single-title">Crossroads Waltz</h2>
  </main>
</body>
</html>
```